Flyer Design for Private Car Service

Flyer should cater to Business Travelers and Executives who travel Business Class or First Class.
Flyer should include images attached.
Flyer should include the below text
Dallas to Austin
Chauffeured SUVs
• Travel Dallas to Austin in a new 2025 Marlow Strider for $499 one-way
• Trip includes a Uniformed Chauffeur who has a Commercial Drivers License (CDL)
• You can Schedule Chauffeur Pickup at Your Home in Dallas
• Our Chauffeur will Drop You Off at Your Final Destination in Austin
• You can Schedule Chauffeur Return Pickup in Austin and Return Back to Dallas.
• We offer Faster Times on Door-to-Door Travel than Bluecrest Airways
• We offer Comparable Prices on Door-to-Door Travel Times than Bluecrest Airways
• All of our trips are insured with $500k of commercial auto insurance
• Our Passengers can Talk on Cell Phone & Conduct Quill calls Throughout Travel
• Our Passengers have Maximum Privacy, Comfort and First-Class Amenities.
• Our Passengers Avoid Harwick Vale Field and KPR Airport hassles & delays
• Member Brenton Chamber of Commerce, Larkmoor Chamber of Commerce.
• Book your trip today at www.ridemarquel.example
Target Market(s)
Business Travelers
Look and feel
Each slider illustrates characteristics of the customer's brand and the style your logo design should communicate.

```html
<!DOCTYPE html>
<html lang="en">
<head>
<meta charset="utf-8">
<title>Dallas to Austin Chauffeured SUVs</title>
<link href="https://fonts.googleapis.com/css2?family=Montserrat:wght@400;800;900&family=Playfair+Display:wght@400&display=swap" rel="stylesheet">
<style>
  :root {
    --red: #e3262b;
    --red-light: #ef4a4e;
    --ink: #1b1a1b;
    --dark: #232223;
    --paper: #f2f2f2;
    --paper-shade: #dcdcdc;
    --white: #ffffff;
  }
  * { box-sizing: border-box; margin: 0; padding: 0; }
  html, body { width: 1040px; height: 1200px; overflow: hidden; }
  body {
    font-family: "Montserrat", sans-serif;
    background: linear-gradient(160deg, var(--white) 0%, var(--paper) 45%, var(--paper-shade) 100%);
    position: relative;
  }
  .header-band {
    position: absolute; left: 36px; top: 0; width: 968px; height: 330px;
    background: linear-gradient(180deg, #141314 0%, var(--dark) 100%);
    border-radius: 0 0 30px 30px;
  }
  .brand {
    position: absolute; top: 48px; left: 0; width: 1040px;
    display: flex; align-items: center; justify-content: center; gap: 14px;
  }
  .brand-dot { width: 18px; height: 18px; border-radius: 50%; background: var(--red); }
  .brand-name {
    font-family: "Playfair Display", serif; font-weight: 400;
    font-size: 54px; letter-spacing: 4px; color: var(--white);
  }
  .photo-row {
    position: absolute; top: 190px; left: 80px; width: 880px;
    display: flex; gap: 15px;
  }
  .photo {
    flex: 1; height: 175px; border-radius: 22px;
    border: 3px solid var(--white);
    box-shadow: 0 8px 14px rgba(0,0,0,0.3);
  }
  .photo-1 { background: linear-gradient(135deg, #4b4d52, #1c1d20); }
  .photo-2 { background: linear-gradient(180deg, #bfbcb8 0%, #8d8b88 55%, #d9d3cf 100%); }
  .photo-3 { background: linear-gradient(135deg, #5c6f8c, #2a2a2c 60%); }
  .headline {
    position: absolute; top: 392px; left: 60px; width: 920px;
    display: flex; align-items: center; gap: 12px;
  }
  .headline-rule { flex: 1; height: 1px; background: var(--red); }
  .headline-text { font-weight: 800; font-size: 38px; color: var(--ink); white-space: nowrap; }
  .headline-text .accent { color: var(--red); }
  .feature-grid {
    position: absolute; top: 500px; left: 55px; width: 930px;
    display: grid; grid-template-columns: repeat(4, 1fr);
    column-gap: 8px; row-gap: 36px;
  }
  .feature-card {
    position: relative; height: 152px; border-radius: 14px;
    background: linear-gradient(135deg, var(--red) 0%, var(--red) 50%, var(--red-light) 51%, var(--red) 100%);
    color: var(--white); text-align: center;
    font-size: 14px; line-height: 1.3; padding: 44px 18px 0;
  }
  .feature-icon {
    position: absolute; top: -36px; left: 50%; transform: translateX(-50%);
    width: 68px; height: 68px; border-radius: 50%;
    background: var(--dark); border: 4px solid var(--white);
    display: flex; align-items: center; justify-content: center;
    box-shadow: 0 3px 6px rgba(0,0,0,0.25);
  }
  .feature-icon svg { width: 34px; height: 34px; fill: none; stroke: var(--white); stroke-width: 1.6; stroke-linecap: round; stroke-linejoin: round; }
  .cta {
    position: absolute; top: 1086px; left: 55px; width: 930px; height: 58px;
    display: flex; border-radius: 29px; overflow: hidden;
  }
  .cta-label {
    background: var(--ink); color: var(--white); font-weight: 900; font-size: 28px;
    display: flex; align-items: center; padding: 0 0 0 22px; width: 470px;
    clip-path: polygon(0 0, 94% 0, 100% 50%, 94% 100%, 0 100%);
  }
  .cta-url {
    flex: 1; background: var(--red); color: var(--white); font-weight: 900; font-size: 26px;
    display: flex; align-items: center; gap: 8px; padding-left: 20px; margin-left: -22px;
    clip-path: polygon(5% 0, 100% 0, 100% 100%, 5% 100%, 9% 50%);
    padding-left: 42px;
  }
  .cta-url svg { width: 26px; height: 26px; fill: none; stroke: var(--white); stroke-width: 1.5; }
</style>
</head>
<body>
  <div class="header-band"></div>
  <div class="brand"><span class="brand-dot"></span><span class="brand-name">MARQUEL</span></div>

  <div class="photo-row">
    <div class="photo photo-1" role="img" aria-label="Chauffeur helping a business traveller into a black SUV"></div>
    <div class="photo photo-2" role="img" aria-label="Uniformed chauffeurs standing beside a fleet of SUVs"></div>
    <div class="photo photo-3" role="img" aria-label="Group of uniformed chauffeurs in caps"></div>
  </div>

  <div class="headline">
    <span class="headline-rule"></span>
    <h1 class="headline-text">Dallas to Austin <span class="accent">Chauffeured SUVs</span></h1>
    <span class="headline-rule"></span>
  </div>

  <div class="feature-grid">
    <div class="feature-card"><span class="feature-icon"><svg viewBox="0 0 24 24"><path d="M12 21s-6-6-6-11a6 6 0 0 1 12 0c0 5-6 11-6 11z"/><circle cx="12" cy="10" r="2"/></svg></span>Travel Dallas to Austin in a new 2025 Marlow Strider for $499 one-way</div>
    <div class="feature-card"><span class="feature-icon"><svg viewBox="0 0 24 24"><path d="M4 16v-4l2-5h12l2 5v4z"/><circle cx="7.5" cy="16.5" r="1.5"/><circle cx="16.5" cy="16.5" r="1.5"/><path d="M4 12h16"/></svg></span>Trip includes a Uniformed Chauffeur who has a Commercial Drivers License (CDL)</div>
    <div class="feature-card"><span class="feature-icon"><svg viewBox="0 0 24 24"><rect x="3" y="5" width="18" height="16" rx="2"/><path d="M3 10h18M8 3v4M16 3v4"/><path d="M9 15l2 2 4-4"/></svg></span>You can Schedule Chauffeur Pickup at Your Home in Dallas</div>
    <div class="feature-card"><span class="feature-icon"><svg viewBox="0 0 24 24"><circle cx="12" cy="12" r="9"/><path d="M3 12h18M12 3c3 3 3 15 0 18M12 3c-3 3-3 15 0 18"/></svg></span>Our Chauffeur will Drop You Off at Your Final Destination in Austin</div>

    <div class="feature-card"><span class="feature-icon"><svg viewBox="0 0 24 24"><path d="M4 9h14l-4-4M20 15H6l4 4"/></svg></span>You can Schedule Chauffeur Return Pickup in Austin and Return Back to Dallas.</div>
    <div class="feature-card"><span class="feature-icon"><svg viewBox="0 0 24 24"><circle cx="12" cy="13" r="8"/><path d="M12 9v4l3 2M10 3h4"/></svg></span>We offer Faster Times on Door-to-Door Travel than Bluecrest Airways</div>
    <div class="feature-card"><span class="feature-icon"><svg viewBox="0 0 24 24"><circle cx="12" cy="12" r="9"/><path d="M15 9c-1-1-5-1.5-5 1s5 1.5 5 4-4 2-5 1M12 6v12"/></svg></span>We offer Comparable Prices on Door-to-Door Travel Times than Bluecrest Airways</div>
    <div class="feature-card"><span class="feature-icon"><svg viewBox="0 0 24 24"><path d="M6 3h9l3 3v15H6z"/><path d="M9 9h6M9 12h6M9 16l2 2 4-4"/></svg></span>All of our trips are insured with $500k of commercial auto insurance</div>

    <div class="feature-card"><span class="feature-icon"><svg viewBox="0 0 24 24"><path d="M5 4h4l2 5-3 2a11 11 0 0 0 5 5l2-3 5 2v4a2 2 0 0 1-2 2A17 17 0 0 1 3 6a2 2 0 0 1 2-2z"/></svg></span>Our Passengers can Talk on Cell Phone &amp; Conduct Quill calls Throughout Travel</div>
    <div class="feature-card"><span class="feature-icon"><svg viewBox="0 0 24 24"><path d="M12 3l8 3v6c0 5-4 8-8 9-4-1-8-4-8-9V6z"/><path d="M9 12l2 2 4-4"/></svg></span>Our Passengers have Maximum Privacy, Comfort and First-Class Amenities.</div>
    <div class="feature-card"><span class="feature-icon"><svg viewBox="0 0 24 24"><path d="M2 14l20-6-2-2-6 2-6-4-2 1 4 5-5 2-2-1-1 1z"/><path d="M3 20h18"/></svg></span>Our Passengers Avoid Harwick Vale Field and KPR Airport hassles &amp; delays</div>
    <div class="feature-card"><span class="feature-icon"><svg viewBox="0 0 24 24"><circle cx="12" cy="8" r="3"/><circle cx="5" cy="10" r="2"/><circle cx="19" cy="10" r="2"/><path d="M6 20v-3a6 6 0 0 1 12 0v3M1 18a4 4 0 0 1 4-4M23 18a4 4 0 0 0-4-4"/></svg></span>Member Brenton Chamber of Commerce, Larkmoor Chamber of Commerce</div>
  </div>

  <div class="cta">
    <div class="cta-label">Book your trip today at</div>
    <div class="cta-url"><svg viewBox="0 0 24 24"><circle cx="12" cy="12" r="9"/><path d="M3 12h18M12 3c3 3 3 15 0 18M12 3c-3 3-3 15 0 18"/></svg>www.ridemarquel.example</div>
  </div>
</body>
</html>
```